Moravel Stenwick Inc needs a business card design

Looking for a unique, classy and sharp business card design.

Contact Information for Business Card

Moravel Stenwick Inc.
Marisa Ortega Bellido BScOT(c)
Occupational Therapist
(780) 555-0142
moravelstenwick@postlynx.net

```html
<!DOCTYPE html>
<html lang="en">
<head>
<meta charset="utf-8">
<title>Moravel Stenwick Inc. — Business Card</title>
<link rel="stylesheet" href="https://fonts.googleapis.com/css2?family=Montserrat:wght@400;500;700&display=swap">
<style>
  :root {
    --page-bg: #f5fde6;
    --card-bg: #ffffff;
    --brand-green: #8dc63f;
    --brand-purple: #8a2a8c;
    --ink: #111111;
    --faint-green: #f1f8ea;
  }
  * { margin: 0; padding: 0; box-sizing: border-box; }
  html, body {
    width: 1200px;
    height: 1200px;
    overflow: hidden;
    background: var(--page-bg);
    font-family: "Montserrat", sans-serif;
  }
  .card {
    position: absolute;
    left: 180px;
    top: 360px;
    width: 840px;
    height: 480px;
    background: var(--card-bg);
    overflow: hidden;
  }
  .card__decor {
    position: absolute;
    right: -120px;
    top: 40px;
    width: 420px;
    height: 420px;
    border-radius: 50%;
    background: var(--faint-green);
  }
  .brand {
    position: absolute;
    left: 50px;
    top: 150px;
    display: flex;
    align-items: center;
    gap: 12px;
  }
  .brand__dot {
    width: 22px;
    height: 22px;
    border-radius: 50%;
    background: var(--brand-green);
  }
  .brand__name {
    font-size: 30px;
    font-weight: 700;
    color: var(--brand-purple);
    letter-spacing: -0.5px;
  }
  .person {
    position: absolute;
    left: 50px;
    top: 340px;
  }
  .person__name {
    font-size: 23px;
    font-weight: 700;
    color: var(--brand-green);
    line-height: 1.2;
  }
  .person__title {
    font-size: 20px;
    font-weight: 500;
    color: var(--ink);
    line-height: 1.3;
  }
  .contact {
    position: absolute;
    left: 50px;
    top: 404px;
    display: flex;
    gap: 48px;
    font-size: 20px;
    font-weight: 500;
    color: var(--ink);
  }
  .contact__item {
    display: flex;
    align-items: center;
    gap: 14px;
  }
  .contact__icon { width: 26px; height: 24px; fill: var(--brand-green); }
</style>
</head>
<body>
  <div class="card">
    <div class="card__decor" aria-hidden="true"></div>

    <div class="brand">
      <span class="brand__dot" aria-hidden="true"></span>
      <span class="brand__name">Moravel Stenwick Inc.</span>
    </div>

    <div class="person">
      <p class="person__name">Marisa Ortega Bellido BScOT(c)</p>
      <p class="person__title">Occupational Therapist</p>
    </div>

    <div class="contact">
      <div class="contact__item">
        <svg class="contact__icon" viewBox="0 0 24 24" aria-hidden="true">
          <path d="M6.6 10.8a15.1 15.1 0 0 0 6.6 6.6l2.2-2.2a1 1 0 0 1 1-.25 11.4 11.4 0 0 0 3.6.57 1 1 0 0 1 1 1V20a1 1 0 0 1-1 1A17 17 0 0 1 3 4a1 1 0 0 1 1-1h3.5a1 1 0 0 1 1 1c0 1.25.2 2.45.57 3.57a1 1 0 0 1-.25 1z"/>
        </svg>
        <span>(780) 555-0142</span>
      </div>
      <div class="contact__item">
        <svg class="contact__icon" viewBox="0 0 26 20" aria-hidden="true">
          <path d="M0 2a2 2 0 0 1 2-2h22a2 2 0 0 1 2 2v.6L13 10 0 2.6z"/>
          <path d="M0 5l13 7.4L26 5v13a2 2 0 0 1-2 2H2a2 2 0 0 1-2-2z"/>
        </svg>
        <span>moravelstenwick@postlynx.net</span>
      </div>
    </div>
  </div>
</body>
</html>
```